Bluegate Wound Care and Hyperbarics Website Refresh

I want to revamp my current website to be more streamlined and look cleaner. I am also adding additional service lines and another location to the company so I would like that added as well. I want to stick with the same logo and colors, but just have it cleaned up with a better overall design.

www.bghyperbarics-example.com

Target Market(s)

Wound Care and Hyperbaric Patients

Industry/Entity Type

Healthcare

Coding

Coded - Design and coding required

Number of Pages Required

5+ page

Colors
0054AA
0677BA
7BADD7
CADEEF
E8F1F8
59FF00
82FF00
B8FF75
E3FFCB
F4FFEA

```html
<!DOCTYPE html>
<html lang="en">
<head>
<meta charset="utf-8">
<title>Bluegate Wound Care &amp; Hyperbarics</title>
<link href="https://fonts.googleapis.com/css2?family=Montserrat:wght@400;500;600;700;800&family=Josefin+Sans:wght@500;600;700&display=swap" rel="stylesheet">
<style>
:root{
  --blue-dark:#0054AA;
  --blue:#0677BA;
  --blue-mid:#7BADD7;
  --blue-light:#CADEEF;
  --blue-pale:#E8F1F8;
  --green:#59B800;
  --green-bright:#6CC417;
  --green-light:#B8FF75;
  --green-pale:#EEFAE0;
  --green-wash:#F4FFEA;
  --ink:#1b1b1b;
  --text:#555;
  --footer:#121212;
}
*{margin:0;padding:0;box-sizing:border-box}
html,body{width:1200px;height:5195px;overflow:hidden}
body{position:relative;background:#fff;font-family:"Montserrat",sans-serif;color:var(--text)}
.abs{position:absolute}
h1,h2,h3{font-family:"Josefin Sans",sans-serif;color:var(--ink);font-weight:600}
.title-center{text-align:center;font-size:32px}
.title-rule{display:block;width:46px;height:10px;margin:4px auto 0;border-top:3px solid var(--blue);border-radius:50%}
.btn{position:absolute;display:flex;align-items:center;gap:12px;height:40px;padding:0 20px 0 8px;border-radius:20px;background:var(--blue-dark);color:#fff;font-size:12.5px;font-weight:500}
.btn::before{content:"";width:26px;height:26px;border-radius:50%;background:#fff;box-shadow:inset 0 0 0 5px var(--blue)}
.btn.green{background:var(--green-bright)}
.btn.green::before{box-shadow:inset 0 0 0 5px var(--green-bright)}
.photo{position:absolute}

/* header & hero */
.hero{position:absolute;left:0;top:0;width:1200px;height:545px;background:linear-gradient(90deg,#f3f4f6 0%,#e9ecef 45%,#dfe3e6 100%);overflow:hidden}
.hero-photo{left:560px;top:0;width:640px;height:545px;background:radial-gradient(ellipse at 60% 45%,#cfd3d6 0%,#9fa5ab 45%,#4c545b 100%)}
.logo{position:absolute;left:161px;top:6px;font-family:"Montserrat",sans-serif;color:var(--ink)}
.logo .name{font-size:34px;font-weight:700;letter-spacing:1px;line-height:38px}
.logo .tag{font-size:9.5px;font-weight:700;margin-left:58px}
.nav{position:absolute;left:502px;top:18px;display:flex;gap:26px;font-size:13.5px;color:var(--ink)}
.nav .active{color:var(--blue);border-bottom:2px solid var(--blue);padding-bottom:2px}
.social{position:absolute;left:873px;top:8px;display:flex;gap:9px}
.social span{width:34px;height:34px;border-radius:50%;border:3px solid var(--blue);background:#fff}
.hero h1{position:absolute;left:163px;top:130px;font-family:"Montserrat",sans-serif;font-weight:800;font-size:49px;line-height:61px;letter-spacing:1px}
.hero .sub{position:absolute;left:164px;top:256px;font-size:19px;color:#333;letter-spacing:.5px}

/* about */
.about-circle{left:175px;top:577px;width:415px;height:415px;border-radius:50%;background:#f4f5f6}
.about-photo{left:213px;top:610px;width:340px;height:340px;border-radius:50%;border:6px solid var(--blue);background:linear-gradient(160deg,#dfe6ee,#9ab0c4 60%,#5c6f83)}
.badge-dot{position:absolute;border-radius:50%;background:#fff;box-shadow:0 4px 12px rgba(0,0,0,.12)}
.eyebrow{font-size:15px;color:#333}
.section-h{font-size:31px}
.para{font-size:13.3px;line-height:24.5px;text-align:justify}

/* services */
.services{position:absolute;left:0;top:1040px;width:1200px;height:810px;background:var(--green-wash)}
.svc{position:absolute;width:240px;text-align:center}
.svc .icon{width:116px;height:116px;margin:0 auto;border-radius:50%;border:2px dashed #c9d3c1;background:#fff;display:flex;align-items:center;justify-content:center}
.svc .icon i{width:72px;height:72px;border-radius:50%;background:linear-gradient(135deg,var(--blue-pale),#d8e6d0)}
.svc h3{font-family:"Montserrat",sans-serif;font-weight:500;font-size:13.5px;color:#222;margin-top:14px;line-height:18px}
.svc p{font-size:12px;line-height:17px;margin-top:4px;color:#666}

/* ceo */
.ceo-ring{left:578px;top:1858px;width:410px;height:410px;border-radius:50%;background:#f3f4f5}
.ceo-photo{left:633px;top:1891px;width:300px;height:300px;border-radius:50%;border:6px solid var(--blue);background:linear-gradient(170deg,#c9b79a,#5c6f8e 55%,#2b3f7a)}
.mini{position:absolute;width:80px;height:80px;border-radius:50%;border:4px solid #fff;box-shadow:0 0 0 2px var(--green-bright);background:linear-gradient(150deg,#e6ecf1,#8fa3b6)}
.arrow-btn{position:absolute;width:36px;height:36px;border-radius:50%;display:flex;align-items:center;justify-content:center}

/* blog */
.blog{position:absolute;left:0;top:2300px;width:1200px;height:715px;background:#eef3f9}
.card{position:absolute;top:215px;width:277px;height:369px;background:#fff;box-shadow:0 6px 16px rgba(0,0,0,.08)}
.card .img{height:171px}
.date{position:absolute;left:0;top:171px;width:42px;height:46px;background:#111;color:#fff;text-align:center;font-size:16px;line-height:16px;padding-top:7px}
.date small{display:block;font-size:11px}
.card h3{position:absolute;left:62px;top:186px;right:14px;font-family:"Josefin Sans",sans-serif;font-size:14.5px;line-height:20px;color:#111;font-weight:600}
.card p{position:absolute;left:62px;top:258px;right:16px;font-size:11.5px;line-height:21px;color:#777}
.card .more{position:absolute;left:62px;top:330px;font-size:12px;color:var(--green);font-weight:600}

/* learn */
.learn-photo{left:121px;top:3040px;width:484px;height:440px;background:radial-gradient(ellipse at 45% 45%,#d9d9d9,#f2f2f2 70%,#fff)}

/* locations */
.locations{position:absolute;left:0;top:3470px;width:1200px;height:810px;background:var(--green-pale)}
.loc{position:absolute;left:182px;width:841px;height:258px;background:#fff;box-shadow:0 4px 14px rgba(0,0,0,.06);border-radius:4px;overflow:hidden}
.map{position:absolute;top:0;width:409px;height:258px;background:linear-gradient(135deg,#eef0ee,#e3e7e1 50%,#f1ead8)}
.loc-item{position:absolute;display:flex;gap:18px;align-items:flex-start}
.loc-ico{width:36px;height:36px;border-radius:50%;border:1.5px solid #ddd;display:flex;align-items:center;justify-content:center;flex:none}
.loc-item b{display:block;font-family:"Josefin Sans",sans-serif;font-weight:600;font-size:14.5px;color:#111}
.loc-item span{font-size:13px;color:#777}
.loc-item .big{font-size:17px;color:#777;letter-spacing:.5px}

/* inquiry & footer */
.footer{position:absolute;left:0;top:4600px;width:1200px;height:595px;background:var(--footer)}
.inquiry{position:absolute;left:272px;top:4327px;width:652px;height:514px;background:#fff;box-shadow:0 6px 20px rgba(0,0,0,.1)}
.field{position:absolute;height:43px;border:1px solid #ccc}
.field label{position:absolute;left:14px;top:-9px;padding:0 16px;background:#fff;font-size:11px;color:#333}
.field span{position:absolute;left:14px;top:12px;font-size:10px;color:#999}
.fcol h4{font-family:"Josefin Sans",sans-serif;font-size:15px;color:#fff;font-weight:600}
.fcol .rule{display:block;width:32px;height:8px;border-top:2px solid var(--blue);border-radius:50%;margin-top:3px}
.fcol ul{list-style:none;font-size:11.5px;color:#ddd;line-height:27px;margin-top:6px}
.fline{display:flex;gap:14px;color:#ddd;font-size:11.5px;line-height:19px}
.copy{position:absolute;left:0;top:5156px;width:1200px;text-align:center;color:#ddd;font-size:12px}
</style>
</head>
<body>

<header class="hero">
  <div class="photo hero-photo" role="img" aria-label="Patient resting inside a hyperbaric oxygen chamber"></div>
  <div class="logo"><div class="name">BLUEGATE</div><div class="tag">Wound Care &amp; Hyperbarics</div></div>
  <nav class="nav"><span class="active">Home</span><span>About</span><span>Services</span><span>Blog</span><span>Contact</span></nav>
  <div class="social" aria-label="Social links"><span></span><span></span><span></span><span></span></div>
  <h1>HYPERBARIC<br>OXYGEN THERAPY</h1>
  <p class="sub">State of the Art Wound Care</p>
  <a class="btn" style="left:161px;top:305px">Learn More</a>
  <svg class="abs" style="left:0;top:340px" width="1200" height="210" viewBox="0 0 1200 210">
    <path d="M0 150 C300 255 760 240 1200 70 L1200 210 L0 210Z" fill="#fff"/>
    <path d="M0 150 C300 255 760 240 1200 70" fill="none" stroke="#6CC417" stroke-width="12"/>
    <path d="M0 25 C250 165 650 200 1200 40 L1200 62 C760 228 300 238 0 140Z" fill="#0054AA"/>
    <path d="M0 25 C250 165 650 200 1200 40" fill="none" stroke="#0677BA" stroke-width="6"/>
  </svg>
</header>

<section aria-label="About us">
  <div class="abs about-circle"></div>
  <div class="photo about-photo" role="img" aria-label="Smiling doctor in white coat with stethoscope"></div>
  <div class="badge-dot" style="left:447px;top:870px;width:76px;height:76px"></div>
  <p class="abs eyebrow" style="left:624px;top:634px">About Us</p>
  <h2 class="abs section-h" style="left:623px;top:662px">Wound Care At Bluegate</h2>
  <p class="abs para" style="left:624px;top:720px;width:414px">Bluegate Wound Care &amp; Hyperbarics is dedicated to the highest level of service with state of the art science for wound care. We are committed to our patient's overall wellbeing and health. We always do what is right for the patient. We will not waiver in our standard of care for our valued customers.</p>
  <a class="btn" style="left:624px;top:890px">Read More</a>
  <svg class="abs" style="left:780px;top:845px" width="180" height="90" viewBox="0 0 180 90"><path d="M170 5 C175 60 110 75 80 70 C60 66 70 45 80 55 C90 68 60 85 10 78" fill="none" stroke="#aaa" stroke-width="1.2"/><path d="M18 72 L8 78 L18 84" fill="none" stroke="#aaa" stroke-width="1.2"/></svg>
</section>

<section class="services" aria-label="Our services">
  <svg class="abs" style="left:0;top:-10px" width="1200" height="80" viewBox="0 0 1200 80"><path d="M0 0 H1200 V55 C900 0 300 -5 0 35Z" fill="#fff"/><path d="M0 35 C300 -5 900 0 1200 55" fill="none" stroke="#B8FF75" stroke-width="3"/></svg>
  <h2 class="abs title-center" style="left:0;top:80px;width:1200px">Our Services<span class="title-rule"></span></h2>
  <svg class="abs" style="left:0;top:0" width="1200" height="700" viewBox="0 0 1200 700">
    <g stroke="#8FCB55" stroke-width="1.5" stroke-dasharray="3 5" fill="none">
      <line x1="380" y1="222" x2="515" y2="240"/><line x1="820" y1="222" x2="690" y2="245"/>
      <line x1="360" y1="420" x2="535" y2="315"/><line x1="601" y1="350" x2="601" y2="400"/><line x1="845" y1="420" x2="665" y2="315"/>
    </g>
    <circle cx="601" cy="257" r="92" fill="#fff" stroke="#6CC417" stroke-width="2" stroke-dasharray="3 6"/>
    <circle cx="601" cy="257" r="66" fill="#E3F5D2"/>
  </svg>
  <div class="svc" style="left:203px;top:150px"><div class="icon" role="img" aria-label="Hyperbaric chamber icon"><i></i></div><h3>Hyperbaric Oxygen<br>Therapy</h3><p>Lorem ipsum dolor sit amet,<br>consectetuer adip elit.</p></div>
  <div class="svc" style="left:761px;top:150px"><div class="icon" role="img" aria-label="Ear icon"><i></i></div><h3>Sensorineural Hearing<br>Loss</h3><p>Lorem ipsum dolor sit amet,<br>consectetuer adip elit.</p></div>
  <div class="svc" style="left:203px;top:405px"><div class="icon" role="img" aria-label="Foot icon"><i></i></div><h3>Diabetic Wound Care</h3><p>Lorem ipsum dolor sit amet,<br>consectetuer adip elit.</p></div>
  <div class="svc" style="left:481px;top:405px"><div class="icon" role="img" aria-label="Bandaged hand icon"><i></i></div><h3>infection healing</h3><p>Lorem ipsum dolor sit amet,<br>consectetuer adip elit.</p></div>
  <div class="svc" style="left:761px;top:405px"><div class="icon" role="img" aria-label="Scalpel icon"><i></i></div><h3>Surgical Wound And<br>Incision Care</h3><p>Lorem ipsum dolor sit amet,<br>consectetuer adip elit.</p></div>
  <a class="btn" style="left:522px;top:630px">Read More</a>
  <svg class="abs" style="left:0;top:755px" width="1200" height="60" viewBox="0 0 1200 60"><path d="M0 40 C300 -10 900 -5 1200 30 V60 H0Z" fill="#fff"/><path d="M0 40 C300 -10 900 -5 1200 30" fill="none" stroke="#B8FF75" stroke-width="3"/></svg>
</section>

<section aria-label="About the chief executive">
  <h2 class="abs section-h" style="left:161px;top:1944px">About Daniel R Moss</h2>
  <span class="abs" style="left:163px;top:1982px;width:36px;height:8px;border-top:3px solid var(--blue);border-radius:50%"></span>
  <p class="abs" style="left:162px;top:2006px;font-size:14.5px;color:#222;font-weight:500">Chief Executive Officer</p>
  <p class="abs para" style="left:162px;top:2030px;width:405px;text-align:left;line-height:27px;font-size:13px">Realizing the need for underutilized ancillary healthcare services like hyperbaric therapy, Daniel founded Bluegate Wound Care and Hyperbarics.</p>
  <div class="arrow-btn" style="left:162px;top:2132px;background:var(--green-bright)"><svg width="14" height="10" viewBox="0 0 14 10"><path d="M13 5H2M6 1L2 5L6 9" stroke="#fff" stroke-width="1.6" fill="none"/></svg></div>
  <div class="arrow-btn" style="left:208px;top:2132px;background:#222"><svg width="14" height="10" viewBox="0 0 14 10"><path d="M1 5H12M8 1L12 5L8 9" stroke="#fff" stroke-width="1.6" fill="none"/></svg></div>
  <div class="abs ceo-ring"></div>
  <div class="photo ceo-photo" role="img" aria-label="Portrait of the chief executive in a blue suit"></div>
  <div class="badge-dot" style="left:660px;top:2130px;width:70px;height:70px"></div>
  <div class="mini" style="left:956px;top:1900px" role="img" aria-label="Doctor photo"></div>
  <div class="mini" style="left:989px;top:2021px" role="img" aria-label="Hyperbaric chamber photo"></div>
  <div class="mini" style="left:952px;top:2142px" role="img" aria-label="Medical team photo"></div>
  <a class="btn" style="left:516px;top:2239px">More About Us</a>
</section>

<section class="blog" aria-label="Latest blog posts">
  <svg class="abs" style="left:0;top:-10px" width="1200" height="60" viewBox="0 0 1200 60"><path d="M0 0 H1200 V50 C900 5 300 0 0 20Z" fill="#fff"/><path d="M0 20 C300 0 900 5 1200 50" fill="none" stroke="#CADEEF" stroke-width="3"/></svg>
  <h2 class="abs title-center" style="left:0;top:130px;width:1200px">Latest Blog Posts<span class="title-rule"></span></h2>
  <article class="card" style="left:161px"><div class="img" role="img" aria-label="Gloved hands examining a foot" style="background:linear-gradient(135deg,#f1ede8,#d9c6b8)"></div><div class="date">12<small>Jan</small></div><h3>3 Tips To Prevent Diabetic Ulcers: When To Consider Hyperbaric Therapy</h3><p>People with diabetes are more prone to infected wounds and diabetic ulcers....</p><span class="more">Read More ➜</span></article>
  <article class="card" style="left:462px"><div class="img" role="img" aria-label="Interior of a hyperbaric chamber" style="background:linear-gradient(135deg,#7a8580,#c46a35 70%,#e08a4a)"></div><div class="date">12<small>Jan</small></div><h3>Autism, Cerebral Palsy Fibromyalgia: 3 Lesser-Known Reasons To Consider HBOT</h3><p>Hyperbaric oxygen therapy (HBOT) provides pure oxygen in a pressurized chamber....</p><span class="more">Read More ➜</span></article>
  <article class="card" style="left:762px"><div class="img" role="img" aria-label="Neon illustration about anemia" style="background:linear-gradient(135deg,#1b2a6b,#b0284a 60%,#e0a030)"></div><div class="date">12<small>Jan</small></div><h3>3 Reasons Anemic Patients May Consider Hyperbaric Treatment</h3><p>Hyperbaric treatment can be beneficial for anemia patients, in specific cases....</p><span class="more">Read More ➜</span></article>
  <a class="btn" style="left:534px;top:625px">View All</a>
  <svg class="abs" style="left:0;top:690px" width="1200" height="30" viewBox="0 0 1200 30"><path d="M0 25 C400 0 800 0 1200 15 V30 H0Z" fill="#fff"/></svg>
</section>

<section aria-label="Learn more">
  <div class="photo learn-photo" role="img" aria-label="Smiling receptionist wearing a headset"></div>
  <h2 class="abs section-h" style="left:622px;top:3120px">Learn More Today!</h2>
  <p class="abs" style="left:623px;top:3176px;width:410px;font-size:13.5px;line-height:28px;color:#444">Ipsum Is Simply Dummy Text Of The Printing And Typesetting Industry.  Lorem Ipsum Standard Dummy Text Ever To Make A Type Specimen Book.</p>
  <p class="abs" style="left:623px;top:3276px;font-size:13.5px;color:#222;font-weight:600">Give us a call to schedule a consult.</p>
  <div class="abs" style="left:630px;top:3325px;width:46px;height:46px;border-radius:50%;background:var(--blue);box-shadow:0 0 0 5px var(--blue-light);display:flex;align-items:center;justify-content:center"><svg width="22" height="22" viewBox="0 0 24 24"><path d="M6.6 10.8a15 15 0 0 0 6.6 6.6l2.2-2.2c.3-.3.7-.4 1-.2 1.1.4 2.3.6 3.6.6.6 0 1 .4 1 1V20c0 .6-.4 1-1 1A17 17 0 0 1 3 4c0-.6.4-1 1-1h3.5c.6 0 1 .4 1 1 0 1.3.2 2.5.6 3.6.1.3 0 .7-.2 1z" fill="#fff"/></svg></div>
  <p class="abs" style="left:690px;top:3338px;font-size:15.5px;font-weight:600;color:#222;text-decoration:underline">555-014-2231</p>
  <svg class="abs" style="left:800px;top:3255px" width="170" height="100" viewBox="0 0 170 100"><path d="M155 5 C165 60 110 85 80 78 C60 74 70 52 80 62 C88 74 60 92 15 88" fill="none" stroke="#aaa" stroke-width="1.2"/><path d="M22 82 L12 88 L22 94" fill="none" stroke="#aaa" stroke-width="1.2"/></svg>
</section>

<section class="locations" aria-label="Our locations">
  <svg class="abs" style="left:0;top:-15px" width="1200" height="70" viewBox="0 0 1200 70"><path d="M0 0 H1200 V10 C900 30 300 40 0 60Z" fill="#fff"/><path d="M0 60 C300 40 900 30 1200 10" fill="none" stroke="#59B800" stroke-width="5"/></svg>
  <h2 class="abs title-center" style="left:0;top:70px;width:1200px">Our Locations<span class="title-rule"></span></h2>
  <div class="loc" style="top:145px">
    <div class="map" style="left:0" role="img" aria-label="Street map of the first clinic area"></div>
    <div class="loc-item" style="left:448px;top:42px"><div class="loc-ico"><svg width="14" height="18" viewBox="0 0 14 18"><path d="M7 0C3 0 0 3 0 7c0 5 7 11 7 11s7-6 7-11c0-4-3-7-7-7zm0 9.5A2.5 2.5 0 1 1 7 4.5a2.5 2.5 0 0 1 0 5z" fill="#333"/></svg></div><div><b>Bluegate Wound Care &amp; Hyperbarics</b><span>4820 Meridian Pkwy, Suite 210, Plano, TX 75024</span></div></div>
    <div class="loc-item" style="left:448px;top:110px"><div class="loc-ico"><svg width="16" height="16" viewBox="0 0 24 24"><path d="M6.6 10.8a15 15 0 0 0 6.6 6.6l2.2-2.2c.3-.3.7-.4 1-.2 1.1.4 2.3.6 3.6.6.6 0 1 .4 1 1V20c0 .6-.4 1-1 1A17 17 0 0 1 3 4c0-.6.4-1 1-1h3.5c.6 0 1 .4 1 1 0 1.3.2 2.5.6 3.6.1.3 0 .7-.2 1z" fill="#333"/></svg></div><div><b>Call No:</b><span class="big">555-014-2231</span></div></div>
    <div class="loc-item" style="left:448px;top:180px"><div class="loc-ico"><svg width="16" height="16" viewBox="0 0 16 16"><rect x="4" y="1" width="8" height="4" fill="#333"/><rect x="1" y="5" width="14" height="7" rx="1" fill="#333"/><rect x="4" y="10" width="8" height="5" fill="#fff" stroke="#333"/></svg></div><div><b>Fax No:</b><span class="big">555-014-2298</span></div></div>
  </div>
  <div class="loc" style="top:419px">
    <div class="map" style="left:432px" role="img" aria-label="Street map of the second clinic area"></div>
    <div class="loc-item" style="left:26px;top:42px"><div class="loc-ico"><svg width="14" height="18" viewBox="0 0 14 18"><path d="M7 0C3 0 0 3 0 7c0 5 7 11 7 11s7-6 7-11c0-4-3-7-7-7zm0 9.5A2.5 2.5 0 1 1 7 4.5a2.5 2.5 0 0 1 0 5z" fill="#333"/></svg></div><div><b>Bluegate Wound Care &amp; Hyperbarics</b><span>123, Building Name Street City, State XY 123456</span></div></div>
    <div class="loc-item" style="left:26px;top:110px"><div class="loc-ico"><svg width="16" height="16" viewBox="0 0 24 24"><path d="M6.6 10.8a15 15 0 0 0 6.6 6.6l2.2-2.2c.3-.3.7-.4 1-.2 1.1.4 2.3.6 3.6.6.6 0 1 .4 1 1V20c0 .6-.4 1-1 1A17 17 0 0 1 3 4c0-.6.4-1 1-1h3.5c.6 0 1 .4 1 1 0 1.3.2 2.5.6 3.6.1.3 0 .7-.2 1z" fill="#333"/></svg></div><div><b>Call No:</b><span class="big">123-456-7890</span></div></div>
    <div class="loc-item" style="left:26px;top:180px"><div class="loc-ico"><svg width="16" height="16" viewBox="0 0 16 16"><rect x="4" y="1" width="8" height="4" fill="#333"/><rect x="1" y="5" width="14" height="7" rx="1" fill="#333"/><rect x="4" y="10" width="8" height="5" fill="#fff" stroke="#333"/></svg></div><div><b>Fax No:</b><span class="big">123-456-7890</span></div></div>
  </div>
  <svg class="abs" style="left:0;top:760px" width="1200" height="60" viewBox="0 0 1200 60"><path d="M0 50 C300 20 900 10 1200 0 V60 H0Z" fill="#fff"/><path d="M0 50 C300 20 900 10 1200 0" fill="none" stroke="#59B800" stroke-width="5"/></svg>
</section>

<footer class="footer">
  <svg class="abs" style="left:0;top:-20px" width="1200" height="80" viewBox="0 0 1200 80"><path d="M0 0 H1200 V0 C900 10 300 30 0 70Z" fill="#fff"/><path d="M0 70 C300 30 900 10 1200 0" fill="none" stroke="#6CC417" stroke-width="6"/></svg>
  <div class="fcol abs" style="left:162px;top:300px"><h4>Quick Links</h4><span class="rule"></span><ul><li>Home</li><li>About</li><li>Services</li><li>Blog</li><li>Contact</li></ul></div>
  <div class="abs" style="left:310px;top:310px;height:190px;border-left:1px dashed #444"></div>
  <div class="fcol abs" style="left:387px;top:302px;width:240px"><h4>Contact Details</h4><span class="rule"></span>
    <div class="fline" style="margin-top:16px"><svg width="12" height="15" viewBox="0 0 14 18"><path d="M7 0C3 0 0 3 0 7c0 5 7 11 7 11s7-6 7-11c0-4-3-7-7-7z" fill="#fff"/></svg><span>ADDRESS:<br>4820 Meridian Pkwy, Suite 210, Plano, TX 75024</span></div>
    <div class="fline" style="margin-top:14px"><svg width="13" height="13" viewBox="0 0 24 24"><path d="M6.6 10.8a15 15 0 0 0 6.6 6.6l2.2-2.2c.3-.3.7-.4 1-.2 1.1.4 2.3.6 3.6.6.6 0 1 .4 1 1V20c0 .6-.4 1-1 1A17 17 0 0 1 3 4c0-.6.4-1 1-1h3.5c.6 0 1 .4 1 1 0 1.3.2 2.5.6 3.6.1.3 0 .7-.2 1z" fill="#fff"/></svg><span>555-014-2231</span></div>
    <div class="fline" style="margin-top:16px"><svg width="13" height="13" viewBox="0 0 16 16"><rect x="4" y="1" width="8" height="4" fill="#fff"/><rect x="1" y="5" width="14" height="7" rx="1" fill="#fff"/></svg><span>555-014-2298</span></div>
  </div>
  <div class="abs" style="left:648px;top:310px;height:190px;border-left:1px dashed #444"></div>
  <div class="abs" style="left:752px;top:330px;color:#555;font-family:Montserrat,sans-serif"><div style="font-size:40px;font-weight:700;letter-spacing:2px;line-height:44px">BLUEGATE</div><div style="font-size:14px;font-weight:700;margin-left:80px">Wound Care &amp; Hyperbarics</div></div>
  <div class="abs" style="left:752px;top:410px;width:286px;border-top:1px dashed #444"></div>
  <div class="abs" style="left:798px;top:425px;display:flex;gap:20px"><span style="width:32px;height:32px;border-radius:50%;border:3px solid #0677BA"></span><span style="width:32px;height:32px;border-radius:50%;border:3px solid #0677BA"></span><span style="width:32px;height:32px;border-radius:50%;border:3px solid #0677BA"></span><span style="width:32px;height:32px;border-radius:50%;border:3px solid #0677BA"></span></div>
  <div class="abs" style="left:0;top:530px;width:1200px;border-top:1px solid #333"></div>
</footer>
<p class="copy">© 2021 Bghyperbarics Medical Woundcare.. All Rights Reserved.</p>

<section class="inquiry" aria-label="Quick inquiry">
  <h2 class="abs title-center" style="left:0;top:55px;width:652px">Quick Inquiry<span class="title-rule"></span></h2>
  <p class="abs" style="left:0;top:120px;width:652px;text-align:center;font-size:13px;color:#333">Let Us Show You The Bluegate Wound Care Difference</p>
  <div class="field" style="left:38px;top:163px;width:282px"><label>First Name</label><span>First Name*</span></div>
  <div class="field" style="left:332px;top:163px;width:282px"><label>Last Name</label><span>Last Name*</span></div>
  <div class="field" style="left:38px;top:231px;width:282px"><label>Email</label><span>Email*</span></div>
  <div class="field" style="left:332px;top:231px;width:282px"><label>Number</label><span>Number*</span></div>
  <div class="field" style="left:38px;top:298px;width:576px;height:82px"><label>How can We Help</label><span>How can We Help*</span></div>
  <a class="btn green" style="left:262px;top:412px">SUBMIT</a>
</section>

</body>
</html>
```